Our company, Brisk Ladle Pantry prepares handmade, wholesome meals fully cooked and ready to he...

We are rolling out a line of Artisan Small Batch Salad dressings. Our initial offering is an herb/Dijon based vinaigrette that has pleased our friends and families for years. We would like to see designs that incorporate the colors in our logo ( Green is 107 165 57, Gray is 72 72 74 ) The final design should communicate freshness, herbs ( parsley, onion, lettuce, cherry tomatoes, olives) that are caricatures or line drawings at the top or left side of the label. Some or all of these veggies can be used depending upon space,layout etc. Space should not be crowded. Note: We anticipate having additional offerings in the future under the "brisk toppings" name such as sauces and marinades. The attached drawing is only a concept drawing and we defer to the designer for layout and creativity. Our company name is Brisk Ladle Pantry and we would like to incorporate a "fork" in this label design

Font styles to use
Decorative
Script

Colors

Designer to choose colors to be used in the design.

Requirements
Must have
• Vegetables should be in a caricature or line drawing format.
Nice to have
• I uploaded an MS word document that contains a head shot photo of the owner. We would like to have a whimsical rendition done that we will add to our left or right panel on the label.

```html
<!DOCTYPE html>
<html lang="en">
<head>
<meta charset="utf-8">
<title>Brisk Toppings – Artisan Vinaigrette Label</title>
<link rel="stylesheet" href="https://fonts.googleapis.com/css2?family=Montserrat:wght@600&family=Playfair+Display:wght@500;800&display=swap">
<style>
  :root {
    --stage: #262626;
    --label: #ffffff;
    --brand-green: #6ba539;
    --panel-green: #8bbd50;
    --brand-gray: #48484a;
    --sketch-light: #e9e9e9;
    --sketch-dark: #9a9a9a;
  }
  html, body {
    margin: 0;
    width: 1200px;
    height: 900px;
    overflow: hidden;
    background: var(--stage);
  }
  .label {
    position: absolute;
    left: 351px;
    top: 207px;
    width: 496px;
    height: 495px;
    background: var(--label);
    overflow: hidden;
  }
  .brand {
    position: absolute;
    top: 24px;
    left: 0;
    width: 100%;
    text-align: center;
  }
  .brand-mark {
    display: block;
    width: 34px;
    height: 34px;
    margin: 0 auto 10px;
    border-radius: 50%;
    background: var(--brand-green);
  }
  .brand-name {
    font-family: "Montserrat", sans-serif;
    font-weight: 600;
    font-size: 21px;
    letter-spacing: 0.5px;
    color: var(--brand-gray);
    text-transform: uppercase;
  }
  .line-title {
    position: absolute;
    left: 0;
    top: 118px;
    width: 496px;
    height: 80px;
  }
  .line-title text {
    font-family: "Playfair Display", serif;
    font-weight: 800;
    font-size: 40px;
    fill: var(--brand-green);
    letter-spacing: 1px;
  }
  .produce-art {
    position: absolute;
    left: 95px;
    top: 180px;
    width: 325px;
    height: 138px;
    border-radius: 40px 40px 10px 10px;
    background: radial-gradient(ellipse at center, var(--sketch-light) 0%, #f5f5f5 60%, var(--label) 100%);
  }
  .product-frame {
    position: absolute;
    left: 0;
    top: 0;
    width: 496px;
    height: 495px;
  }
  .product-info {
    position: absolute;
    left: 21px;
    top: 408px;
    width: 454px;
    text-align: center;
    color: var(--label);
    font-family: "Playfair Display", serif;
  }
  .product-name {
    margin: 0;
    font-weight: 500;
    font-size: 33px;
    line-height: 1;
  }
  .product-volume {
    margin: 16px 0 0;
    font-size: 13px;
  }
</style>
</head>
<body>
  <main class="label">
    <header class="brand">
      <span class="brand-mark"></span>
      <span class="brand-name">Brisk Ladle Pantry</span>
    </header>

    <svg class="line-title" viewBox="0 0 496 80" aria-label="Brisk Toppings">
      <defs>
        <path id="title-arc" d="M30 62 Q248 20 466 62"/>
      </defs>
      <text text-anchor="middle"><textPath href="#title-arc" startOffset="50%">BRISK TOPPINGS</textPath></text>
    </svg>

    <div class="produce-art" role="img" aria-label="Line drawing of lettuce, a bowl of olives, an onion, parsley sprigs and cherry tomatoes"></div>

    <svg class="product-frame" viewBox="0 0 496 495" aria-hidden="true">
      <path d="M9 495 V350 H140 C175 350 185 338 215 336 C250 334 270 344 300 344 H487 V495"
            fill="none" stroke="var(--brand-gray)" stroke-width="4"/>
      <path d="M21 495 V357 H145 C180 357 190 346 218 344 C252 342 272 352 305 352 H475 V495 Z"
            fill="var(--panel-green)"/>
      <g class="fork-icon" fill="var(--label)">
        <rect x="202" y="363" width="42" height="3" rx="1.5"/>
        <rect x="202" y="369.5" width="42" height="3" rx="1.5"/>
        <rect x="202" y="376" width="42" height="3" rx="1.5"/>
        <rect x="202" y="382.5" width="42" height="3" rx="1.5"/>
        <path d="M240 362 H252 C262 362 266 370 272 371 L340 367 C345 367 345 375 340 375 L272 377 C266 378 262 387 252 387 H240 Z"/>
      </g>
    </svg>

    <section class="product-info">
      <h1 class="product-name">Artisan Vinaigrette</h1>
      <p class="product-volume">237 (ml)</p>
    </section>
  </main>
</body>
</html>
```